Furniture Wholesaler PowerPoint Template Refresh

Larkmoor Traders is a family owned and operated furniture wholesaler that works with retailers like Brindle, Quillmart, and Tessgrove to sell multifunctional furniture and home décor pieces.

We are looking for a new company PowerPoint template, primarily to be used by our sales team when working with our new and existing retail partners. Our current slideshow deck is attached below. We would like the new design to have a more modern and minimalist feel with at least 3-4 slide design options.

Our current logo is also included in the old slideshow attached below, but we are not looking to emphasize it in the new PowerPoint design.

Target Market(s)

This presentation will be used by our sales team to inform existing and potential retail partners of our company history, product selections, and fulfillment capabilities.

Industry/Entity Type

Ecommerce

Font styles to use
Other font styles liked:
• Please use Windows system fonts for any text. Our logo font is Myriad Pro, which should only be used for any graphics.

Colors

Designer to choose colors to be used in the design.

Requirements
Must have
• - at least 3-4 slide design options
- redesign of the image on slide 4 in the old presentation (attached below)
- same slide layout options as the old presentation, including a cover slide, title with text slide, title with text and image slide, and title with image slide.
- Blue and white as main colors with red as the accent. RGB codes are:
Blue - R0, G67, B104
White - R255, G255, B255
Red - R181, G36, B25
Should not have
• - do not emphasize our logo in new design (especially the blue ball)

```html
<!DOCTYPE html>
<html lang="en">
<head>
<meta charset="utf-8">
<title>Larkmoor Traders Presentation Deck</title>
<link href="https://fonts.googleapis.com/css2?family=Lobster&family=Poppins:wght@400;600;700&family=Open+Sans:wght@400;600;700&display=swap" rel="stylesheet">
<style>
:root{
  --blue:#004368;
  --blue-deep:#0b3a5c;
  --sky:#1e93d1;
  --red:#b52419;
  --yellow:#f7c21a;
  --white:#ffffff;
  --paper:#e6e7ea;
  --ink:#2a2a2a;
  --mute:#6b7280;
}
*{box-sizing:border-box;margin:0;padding:0}
html,body{width:852px;height:1200px;overflow:hidden;background:var(--paper)}
body{position:relative;font-family:"Open Sans",Arial,sans-serif;color:var(--ink)}
.hero-photo{position:absolute;left:0;top:0;width:852px;height:388px;
  background:linear-gradient(160deg,#c9cdd3 0%,#a9aeb6 40%,#d4d6da 75%);
  clip-path:polygon(0 0,852px 0,852px 30px,0 388px)}
.deck-title{position:absolute;left:50px;top:128px;font-family:"Poppins",Arial,sans-serif;line-height:1}
.deck-title .big{display:block;font-size:42px;font-weight:700;color:var(--blue)}
.deck-title .small{display:block;margin:2px 0 0 90px;font-size:40px;font-weight:400;color:#222}
.divider{position:absolute;left:328px;top:380px;width:180px;height:1px;background:var(--blue)}
.slide{position:absolute;width:273px;height:153px;background:var(--white);overflow:hidden;box-shadow:0 1px 3px rgba(0,0,0,.12)}
.bar-title{position:absolute;left:0;top:0;width:100%;height:25px;background:var(--blue);
  color:var(--white);font-family:"Lobster",cursive;font-size:13.5px;text-align:center;line-height:25px}
.bar-title em,.script em{font-style:normal;color:var(--red)}
.foot{position:absolute;left:0;bottom:0;width:100%;height:10px;background:var(--sky);
  font-size:2.6px;letter-spacing:.6px;color:var(--white);line-height:10px;padding-left:6px;font-weight:600}
.script{font-family:"Lobster",cursive;line-height:1}
.copy{font-size:3.2px;line-height:1.5;color:#444}
.photo{position:absolute}
.ph-room{background:linear-gradient(135deg,#e9e6e1,#b9b3aa 60%,#8c857c)}
.ph-dark{background:linear-gradient(135deg,#3b3d44,#6d6f77 55%,#d9d9dc)}
.ph-blue{background:linear-gradient(135deg,#1c4f73,#0e3b5b 60%,#255a80)}
.ph-light{background:linear-gradient(135deg,#f1f2f4,#d5d8dc)}
.ph-wood{background:linear-gradient(135deg,#e8ddd0,#b08a64 60%,#6f4e33)}
.ph-chair{background:linear-gradient(135deg,#4b5a4a,#cfc9bf 50%,#8f7a60)}
.disc{position:absolute;border-radius:50%;display:flex;flex-direction:column;align-items:center;justify-content:center;
  text-align:center;font-family:"Open Sans",Arial,sans-serif;line-height:1;color:var(--white);box-shadow:0 1px 3px rgba(0,0,0,.3)}
.disc.red{background:var(--red);border:1.5px solid var(--white)}
.disc.blue{background:var(--blue);border:1.5px solid var(--white)}
.brandmark{position:absolute;display:flex;align-items:center;gap:3px;font-family:"Open Sans",Arial,sans-serif;font-weight:700;color:var(--blue)}
.brandmark i{display:block;border-radius:50%;background:var(--blue)}
.spaced{letter-spacing:2px;font-weight:600;color:var(--white);text-align:center}
.socials{position:absolute;display:flex;gap:2px}
.socials i{display:block;border:0.6px solid var(--sky);border-radius:50%}
.tagline{position:absolute;left:60px;top:35px;width:140px;transform:rotate(-29.5deg);transform-origin:50% 50%;
  color:var(--white);font-family:"Poppins",Arial,sans-serif;font-weight:600;font-size:7.6px;line-height:1.25;text-align:center;white-space:nowrap}
.stat-row{position:absolute;left:71px;width:145px;height:30px;display:flex;align-items:center;gap:6px;padding-left:8px;color:var(--white)}
.stat-row .pct{width:17px;height:17px;flex:none;border-radius:50%;font-size:5.5px;font-weight:700;font-style:italic;display:flex;align-items:center;justify-content:center;color:var(--yellow);box-shadow:0 1px 2px rgba(0,0,0,.4)}
.stat-row h4{font-size:4.2px;color:var(--yellow);font-weight:600}
.stat-row p{font-size:2.6px;line-height:1.4;width:100px}
.lbl{position:absolute;width:62px;font-size:2.6px;line-height:1.4;color:#666}
.lbl b{display:block;font-size:4.4px;color:var(--blue);font-weight:600}
.lbl.r{text-align:right}
.panel{position:absolute;background:var(--blue)}
.card{position:absolute;top:60px;width:55px;height:74px;background:var(--blue);padding:14px 7px 0;color:var(--white)}
.card h5{font-size:4.6px;color:var(--yellow);line-height:1.1;font-weight:700;margin-bottom:4px}
.card p{font-size:2.8px;line-height:1.4}
.badge{position:absolute;top:-8px;left:17px;width:19px;height:19px;border-radius:50%;border:1.3px solid var(--white);font-size:4.5px;font-weight:700;display:flex;flex-direction:column;align-items:center;justify-content:center;line-height:1}
.badge small{font-size:1.8px}
.box{position:absolute;background:var(--blue);color:var(--white);padding:8px 10px}
.box h5{font-size:4.6px;color:var(--yellow);margin-bottom:4px;font-weight:700}
.box p{font-size:3px;line-height:1.45}
.tiles{position:absolute;left:10px;top:34px;display:grid;grid-template-columns:repeat(6,36px);grid-auto-rows:19px;gap:6px 7px}
.tile{background:var(--white);box-shadow:0 1px 3px rgba(0,0,0,.18);display:flex;align-items:center;justify-content:center;gap:1.5px;font-size:4.4px;font-weight:700}
.tile i{display:block;width:3px;height:3px}
.t-brindle{color:#6b1e74}.t-brindle i{background:#6b1e74;border-radius:50%}
.t-quill{color:#222}.t-quill i{background:#222}
.t-penn{color:var(--red)}.t-penn i{background:var(--red)}
.t-halv{color:var(--white);background:#0a4d9c}
.mini-stat{position:absolute;left:23px;width:37px;height:31px;border:0.8px solid var(--yellow);border-radius:3px;text-align:center;font-weight:700;line-height:1;
  display:flex;flex-direction:column;align-items:center;justify-content:center;gap:0.5px}
.mini-stat b{display:block;font-size:10px;color:var(--yellow)}
.mini-stat span{display:block;font-size:4.2px;color:var(--red)}
.mini-stat em{display:block;font-style:normal;font-size:4px;color:var(--white);letter-spacing:.8px;font-weight:400}
</style>
</head>
<body>

<div class="hero-photo" role="img" aria-label="Faded photo of friends raising their arms against a sunset sky"></div>
<h1 class="deck-title"><span class="big">Presentation</span><span class="small">Deck</span></h1>

<!-- featured cover slide -->
<section class="slide" style="left:399px;top:61px;width:332px;height:186px">
  <div class="brandmark" style="left:124px;top:6px;font-size:6px"><i style="width:6px;height:6px"></i>LARKMOOR TRADERS</div>
  <div class="photo ph-blue" style="left:0;top:30px;width:332px;height:136px" role="img" aria-label="Blue-toned photo of a living room sofa"></div>
  <p class="spaced" style="position:absolute;left:0;width:100%;top:56px;font-size:4.6px">JUNE, 2020</p>
  <p class="script" style="position:absolute;left:0;width:100%;top:86px;text-align:center;color:var(--white);font-size:22px">Title page | cover</p>
  <p class="spaced" style="position:absolute;left:0;width:100%;top:117px;font-size:4.4px;letter-spacing:2.5px">SUB TITLE GOES HERE</p>
  <div class="socials" style="left:152px;top:173px"><i style="width:7px;height:7px"></i><i style="width:7px;height:7px"></i><i style="width:7px;height:7px"></i></div>
</section>

<div class="divider"></div>

<!-- row 1 -->
<section class="slide" style="left:10px;top:389px">
  <div class="brandmark" style="left:100px;top:9px;font-size:4.4px"><i style="width:5px;height:5px"></i>LARKMOOR TRADERS</div>
  <div class="photo ph-blue" style="left:0;top:25px;width:273px;height:112px" role="img" aria-label="Blue-toned photo of a living room sofa"></div>
  <p class="spaced" style="position:absolute;left:0;width:100%;top:46px;font-size:3.6px">JUNE, 2020</p>
  <p class="script" style="position:absolute;left:0;width:100%;top:71px;text-align:center;color:var(--white);font-size:18px">Title page | cover</p>
  <p class="spaced" style="position:absolute;left:0;width:100%;top:96px;font-size:3.6px">SUB TITLE GOES HERE</p>
  <div class="socials" style="left:125px;top:142px"><i style="width:6px;height:6px"></i><i style="width:6px;height:6px"></i><i style="width:6px;height:6px"></i></div>
</section>

<section class="slide" style="left:290px;top:389px">
  <div class="photo ph-light" style="left:0;top:0;width:273px;height:153px" role="img" aria-label="Pale photo of a bright living room"></div>
  <svg style="position:absolute;left:0;top:0" width="273" height="153" viewBox="0 0 273 153"><path d="M0 0H273L66 116Q60 120 56 114Z" fill="#004368"/></svg>
  <p class="tagline">Excellence in Product Design,<br>Quality, Fulfillment &amp;<br>Customer Service</p>
  <p class="script" style="position:absolute;right:11px;top:109px;color:var(--red);font-size:20px">Making a Difference</p>
</section>

<section class="slide" style="left:569px;top:389px">
  <div class="bar-title">Making A <em>Difference</em></div>
  <div style="position:absolute;left:16px;top:44px;width:242px">
    <p class="copy" style="margin-bottom:4px">Lorem ipsum dolor sit amet, consectetur adipiscing elit, sed do eiusmod tempor incididunt ut labore et dolore magna aliqua. Ut enim ad minim veniam, quis nostrud exercitation ullamco laboris nisi ut aliquip ex ea commodo.</p>
    <p class="copy" style="margin-bottom:4px">Lorem ipsum dolor sit amet, consectetur adipiscing elit, sed do eiusmod tempor incididunt ut labore et dolore magna aliqua. Ut enim ad minim veniam, quis nostrud exercitation ullamco laboris nisi ut aliquip ex ea commodo consequat duis aute.</p>
    <p class="copy" style="margin-bottom:4px">Lorem ipsum dolor sit amet, consectetur adipiscing elit, sed do eiusmod tempor incididunt ut labore et dolore magna aliqua. Ut enim ad minim veniam, quis nostrud exercitation ullamco laboris nisi ut aliquip ex ea commodo consequat. Duis aute irure dolor in reprehenderit in voluptate velit esse cillum dolore eu fugiat nulla pariatur excepteur sint occaecat.</p>
    <p class="copy">Lorem ipsum dolor sit amet, consectetur adipiscing elit, sed do eiusmod tempor incididunt ut labore et dolore magna aliqua ut enim.</p>
  </div>
  <div class="foot">COPYRIGHT © | ALL RIGHTS RESERVED</div>
</section>

<!-- row 2 -->
<section class="slide" style="left:10px;top:551px">
  <div class="bar-title">Making A <em>Difference</em></div>
  <div class="photo ph-room" style="left:6px;top:31px;width:108px;height:106px" role="img" aria-label="Photo of a grey tufted sofa with teal cushions"></div>
  <div class="stat-row" style="left:121px;top:31px;background:var(--red)"><div class="pct" style="background:var(--red)">20%</div><div><h4>Project name</h4><p>Lorem ipsum dolor sit amet, nec an dictas equidem appellantur, ut has commune accommodare.</p></div></div>
  <div class="stat-row" style="left:121px;top:68px;background:var(--blue)"><div class="pct" style="background:var(--blue)">35%</div><div><h4>Project name</h4><p>Lorem ipsum dolor sit amet, nec an dictas equidem appellantur, ut has commune accommodare.</p></div></div>
  <div class="stat-row" style="left:121px;top:105px;background:var(--sky)"><div class="pct" style="background:var(--sky)">80%</div><div><h4>Project name</h4><p>Lorem ipsum dolor sit amet, nec an dictas equidem appellantur, ut has commune accommodare.</p></div></div>
  <div class="foot">COPYRIGHT © | ALL RIGHTS RESERVED</div>
</section>

<section class="slide" style="left:290px;top:551px">
  <div class="bar-title">Making A <em>Difference</em></div>
  <svg style="position:absolute;left:90px;top:40px" width="92" height="92" viewBox="0 0 92 92">
    <g fill="none" stroke-width="17">
      <circle cx="46" cy="46" r="36" stroke="#004368" stroke-dasharray="36 1.7" pathLength="226"/>
      <circle cx="46" cy="46" r="36" stroke="#1e93d1" stroke-dasharray="36 77" stroke-dashoffset="-37.7" pathLength="226"/>
      <circle cx="46" cy="46" r="36" stroke="#1e93d1" stroke-dasharray="36 77" stroke-dashoffset="-150.7" pathLength="226"/>
    </g>
    <circle cx="46" cy="46" r="19" fill="#fff"/>
    <circle cx="46" cy="46" r="16" fill="#004368"/>
    <text x="46" y="48" text-anchor="middle" font-family="Open Sans,Arial,sans-serif" font-weight="700" font-size="4.6" fill="#fff">LARKMOOR</text>
  </svg>
  <div class="lbl r" style="left:30px;top:40px"><b>Lorem ipsum dolor</b>Lorem ipsum dolor sit amet, consectetur adipiscing elit, sed do eiusmod tempor</div>
  <div class="lbl r" style="left:22px;top:78px"><b>Lorem ipsum dolor</b>Lorem ipsum dolor sit amet, consectetur adipiscing elit, sed do eiusmod tempor</div>
  <div class="lbl r" style="left:38px;top:115px"><b>Lorem ipsum dolor</b>Lorem ipsum dolor sit amet, consectetur adipiscing elit, sed do eiusmod tempor</div>
  <div class="lbl" style="left:175px;top:39px"><b>Lorem ipsum dolor</b>Lorem ipsum dolor sit amet, consectetur adipiscing elit, sed do eiusmod tempor</div>
  <div class="lbl" style="left:191px;top:78px"><b>Lorem ipsum dolor</b>Lorem ipsum dolor sit amet, consectetur adipiscing elit, sed do eiusmod tempor</div>
  <div class="lbl" style="left:177px;top:115px"><b>Lorem ipsum dolor</b>Lorem ipsum dolor sit amet, consectetur adipiscing elit, sed do eiusmod tempor</div>
  <div class="foot">COPYRIGHT © | ALL RIGHTS RESERVED</div>
</section>

<section class="slide" style="left:569px;top:551px">
  <div class="panel" style="left:95px;top:0;width:178px;height:143px"></div>
  <p class="copy" style="position:absolute;left:20px;top:36px;width:62px;font-size:2.9px">Lorem ipsum dolor sit amet, consectetur adipiscing elit, sed do eiusmod tempor incididunt ut labore et dolore magna aliqua. Lorem ipsum dolor sit amet, consectetur adipiscing elit, sed do eiusmod tempor incididunt ut labore et dolore magna aliqua.</p>
  <p class="script" style="position:absolute;left:133px;top:26px;color:var(--white);font-size:22px">Making A</p>
  <p class="script" style="position:absolute;left:150px;top:46px;color:var(--red);font-size:20px">Difference</p>
  <div class="photo ph-dark" style="left:19px;top:83px;width:48px;height:46px" role="img" aria-label="Photo of a shelving unit with a white chair"></div>
  <div class="photo ph-dark" style="left:71px;top:83px;width:48px;height:46px" role="img" aria-label="Photo of a shelving unit with a white chair"></div>
  <div class="photo ph-dark" style="left:123px;top:83px;width:48px;height:46px" role="img" aria-label="Photo of a shelving unit with a white chair"></div>
  <div class="photo ph-dark" style="left:175px;top:83px;width:48px;height:46px" role="img" aria-label="Photo of a shelving unit with a white chair"></div>
  <div class="foot">COPYRIGHT © | ALL RIGHTS RESERVED</div>
</section>

<!-- row 3 -->
<section class="slide" style="left:10px;top:713px">
  <div class="bar-title">Making A <em>Difference</em></div>
  <div class="photo ph-chair" style="left:0;top:25px;width:102px;height:118px" role="img" aria-label="Photo of a white lounge chair beside a potted plant"></div>
  <div class="disc red" style="left:82px;top:32px;width:40px;height:40px"><b style="font-size:12px">+18</b><span style="font-size:4.2px;color:var(--yellow)">PRODUCT</span><span style="font-size:3.6px">CATEGORIES</span></div>
  <p class="copy" style="position:absolute;left:131px;top:37px;width:130px">Lorem ipsum dolor sit amet, consectetur adipiscing elit, sed do eiusmod tempor incididunt ut labore et dolore magna aliqua. Ut enim ad minim veniam, quis nostrud exercitation ullamco laboris nisi ut aliquip ex. Lorem ipsum dolor sit amet, consectetur adipiscing elit, sed do eiusmod tempor incididunt ut labore et dolore magna aliqua.</p>
  <p class="copy" style="position:absolute;left:118px;top:94px;width:143px">Lorem ipsum dolor sit amet, consectetur adipiscing elit, sed do eiusmod tempor incididunt ut labore et dolore magna aliqua. Ut enim ad minim veniam, quis nostrud exercitation ullamco laboris nisi ut aliquip ex. Lorem ipsum dolor sit amet, consectetur adipiscing elit, sed do eiusmod tempor incididunt ut labore et dolore magna aliqua.</p>
  <div class="foot">COPYRIGHT © | ALL RIGHTS RESERVED</div>
</section>

<section class="slide" style="left:290px;top:713px">
  <div class="bar-title">Header and A <em>Picture</em></div>
  <div class="photo ph-wood" style="left:43px;top:30px;width:183px;height:108px" role="img" aria-label="Photo of a wooden dining table with chairs"></div>
  <div class="disc red" style="left:209px;top:36px;width:40px;height:40px"><b style="font-size:12px">+18</b><span style="font-size:4.2px;color:var(--yellow)">PRODUCT</span><span style="font-size:3.6px">CATEGORIES</span></div>
  <div class="disc blue" style="left:29px;top:90px;width:40px;height:40px"><b style="font-size:9.5px">1200+</b><span style="font-size:6px;color:var(--yellow)">ACTIVE</span><span style="font-size:6.5px">ITEMS</span></div>
  <div class="foot">COPYRIGHT © | ALL RIGHTS RESERVED</div>
</section>

<section class="slide" style="left:569px;top:713px">
  <div class="panel" style="left:95px;top:0;width:178px;height:143px"></div>
  <div class="photo ph-dark" style="left:22px;top:22px;width:48px;height:46px" role="img" aria-label="Photo of a shelving unit with a white chair"></div>
  <div class="photo ph-dark" style="left:22px;top:83px;width:48px;height:46px" role="img" aria-label="Photo of a shelving unit with a white chair"></div>
  <p class="script" style="position:absolute;left:111px;top:25px;color:var(--white);font-size:17px">Your Awesome</p>
  <p class="script" style="position:absolute;left:179px;top:41px;color:var(--red);font-size:14px">Text Here</p>
  <p class="copy" style="position:absolute;left:111px;top:65px;width:146px;color:var(--white);text-align:justify">Lorem ipsum dolor sit amet, consectetur adipiscing elit, sed do eiusmod tempor incididunt ut labore et dolore magna aliqua. Ut enim ad minim veniam, quis nostrud exercitation ullamco laboris nisi ut aliquip ex. Lorem ipsum dolor sit amet, consectetur adipiscing elit, sed do eiusmod tempor incididunt ut labore et dolore magna aliqua.</p>
  <div style="position:absolute;left:110px;top:113px;width:48px;height:11px;border-radius:6px;background:var(--red);border:1px solid var(--white);color:var(--white);font-size:4.2px;line-height:9px;text-align:center">Your Text Here</div>
  <div class="foot">COPYRIGHT © | ALL RIGHTS RESERVED</div>
</section>

<!-- row 4 -->
<section class="slide" style="left:10px;top:876px">
  <div class="bar-title">Making A <em>Difference</em></div>
  <div class="card" style="left:44px"><div class="badge" style="background:var(--red)">+18<small>PRODUCT</small></div><h5>Add<br>Awesome<br>Title Here</h5><p>Lorem ipsum dolor sit amet, consectetur adipiscing elit, sed do eiusmod tempor incididunt ut labore et dolore magna aliqua.</p></div>
  <div class="card" style="left:109px"><div class="badge" style="background:var(--sky)">+18<small>PRODUCT</small></div><h5>Add<br>Awesome<br>Title Here</h5><p>Lorem ipsum dolor sit amet, consectetur adipiscing elit, sed do eiusmod tempor incididunt ut labore et dolore magna aliqua.</p></div>
  <div class="card" style="left:174px"><div class="badge" style="background:var(--yellow)">+18<small>PRODUCT</small></div><h5>Add<br>Awesome<br>Title Here</h5><p>Lorem ipsum dolor sit amet, consectetur adipiscing elit, sed do eiusmod tempor incididunt ut labore et dolore magna aliqua.</p></div>
  <div class="foot">COPYRIGHT © | ALL RIGHTS RESERVED</div>
</section>

<section class="slide" style="left:290px;top:876px">
  <div class="box" style="left:21px;top:15px;width:116px;height:57px"><h5>Add Awesome Title Here</h5><p>Lorem ipsum dolor sit amet, consectetur adipiscing elit, sed do eiusmod tempor incididunt ut labore et dolore magna aliqua. Lorem ipsum dolor sit amet, consectetur adipiscing elit, sed do eiusmod tempor.</p></div>
  <p class="copy" style="position:absolute;left:150px;top:28px;width:100px">Lorem ipsum dolor sit amet, consectetur adipiscing elit, sed do eiusmod tempor incididunt ut labore et dolore magna aliqua. Lorem ipsum dolor sit amet, consectetur adipiscing elit, sed do eiusmod tempor incididunt ut labore et dolore magna aliqua.</p>
  <p class="script" style="position:absolute;left:34px;top:90px;color:var(--blue);font-size:17px">Making A</p>
  <p class="script" style="position:absolute;left:57px;top:104px;color:var(--red);font-size:14px">Difference</p>
  <div class="box" style="left:139px;top:76px;width:114px;height:57px"><h5>Add Awesome Title Here</h5><p>Lorem ipsum dolor sit amet, consectetur adipiscing elit, sed do eiusmod tempor incididunt ut labore et dolore magna aliqua. Lorem ipsum dolor sit amet, consectetur adipiscing elit, sed do eiusmod tempor.</p></div>
  <div class="foot">COPYRIGHT © | ALL RIGHTS RESERVED</div>
</section>

<section class="slide" style="left:569px;top:876px">
  <div class="bar-title">Omnichannel <em>Fulfillment</em></div>
  <div class="tiles">
    <div class="tile t-brindle"><i></i>Brindle</div><div class="tile t-brindle"><i></i>Brindle</div><div class="tile t-brindle"><i></i>Brindle</div><div class="tile t-brindle"><i></i>Brindle</div><div class="tile t-brindle"><i></i>Brindle</div><div class="tile t-brindle"><i></i>Brindle</div>
    <div class="tile t-quill">Quillmart</div><div class="tile t-quill">Quillmart</div><div class="tile t-quill">Quillmart</div><div class="tile t-quill">Quillmart</div><div class="tile t-quill">Quillmart</div><div class="tile t-quill">Quillmart</div>
    <div class="tile t-penn"><i></i>Pennrow</div><div class="tile t-penn"><i></i>Pennrow</div><div class="tile t-penn"><i></i>Pennrow</div><div class="tile t-penn"><i></i>Pennrow</div><div class="tile t-penn"><i></i>Pennrow</div><div class="tile t-penn"><i></i>Pennrow</div>
    <div class="tile" style="background:none;box-shadow:none"><span class="t-halv" style="padding:2px 3px">HALVARD</span></div><div class="tile" style="background:none;box-shadow:none"><span class="t-halv" style="padding:2px 3px">HALVARD</span></div><div class="tile" style="background:none;box-shadow:none"><span class="t-halv" style="padding:2px 3px">HALVARD</span></div><div class="tile" style="background:none;box-shadow:none"><span class="t-halv" style="padding:2px 3px">HALVARD</span></div><div class="tile" style="background:none;box-shadow:none"><span class="t-halv" style="padding:2px 3px">HALVARD</span></div><div class="tile" style="background:none;box-shadow:none"><span class="t-halv" style="padding:2px 3px">HALVARD</span></div>
  </div>
  <div class="foot">COPYRIGHT © | ALL RIGHTS RESERVED</div>
</section>

<!-- row 5 -->
<section class="slide" style="left:290px;top:1038px">
  <div class="panel" style="left:0;top:0;width:83px;height:143px"></div>
  <p class="script" style="position:absolute;left:6px;top:9px;color:var(--white);font-size:11px">Fulfillment</p>
  <p class="script" style="position:absolute;left:40px;top:19px;color:var(--red);font-size:11px">Experts</p>
  <div class="mini-stat" style="top:35px"><b>45%</b><span>NEXT DAY</span><em>DELIVERY</em></div>
  <div class="mini-stat" style="top:70px"><b>93%</b><span>2 DAYS</span><em>OR LESS</em></div>
  <div class="mini-stat" style="top:105px"><b>100%</b><span>3 DAYS</span><em>OR LESS</em></div>
  <div class="photo" style="left:93px;top:33px;width:170px;height:92px;background:linear-gradient(160deg,#0e4a73,#004368 60%,#1e93d1)" role="img" aria-label="Map of the United States marking warehouse locations in Las Vegas, Dallas and Carlisle"></div>
  <div class="disc red" style="left:118px;top:11px;width:38px;height:38px"><b style="font-size:11px">100%</b><span style="font-size:4px;color:var(--yellow)">SAME DAY</span><span style="font-size:3.4px">SHIPPING</span></div>
  <div class="disc red" style="left:214px;top:5px;width:38px;height:38px"><span style="font-size:4.6px">FASTER</span><span style="font-size:4.6px">DELIVERY</span><span style="font-size:4.2px;color:var(--yellow)">LOWER</span><span style="font-size:4.2px;color:var(--yellow)">COST</span></div>
  <p style="position:absolute;left:93px;top:127px;width:170px;text-align:center;font-size:5px;color:var(--blue);font-weight:600"><span style="color:var(--red)">2-DAY</span> DELIVERY MESSAGING</p>
  <p style="position:absolute;left:93px;top:134px;width:170px;text-align:center;font-size:3px;color:var(--red)">Increases Sales by 25%</p>
  <div class="foot">COPYRIGHT © | ALL RIGHTS RESERVED</div>
</section>

</body>
</html>
```